Redesign of Business Card to look more professional and stand out

Business card design. You can lean more about our company by going to dkrfabworks.example. Raised letters would be nice. Company name & Address
DK&R
418 Wendlow Ridge Drive, Suite 340
Birmingham, AL 35242

You can use my name and title: Glenn Harwick
Business Development Manager

Target Market(s)

Heavy Industrial market, i.e. utilities, chemical plants, paper mills, construction companies

Industry/Entity Type

Construction

Contact Information for Business Card

We provide Project Management & Project Support Services

Font styles to use
Serif

Requirements
Must have
• Company name & Address
• DK&R
• 418 Wendlow Ridge Drive, Suite 340
• Birmingham, AL 35242
Nice to have
• ideas for the back of the card
Should not have
• no crazy colors. needs to look professional and standout.

```html
<!DOCTYPE html>
<html lang="en">
<head>
<meta charset="utf-8">
<title>DK&amp;R Business Card</title>
<link rel="stylesheet" href="https://fonts.googleapis.com/css2?family=Arimo:wght@400;700&display=swap">
<style>
  :root {
    --navy: #1f3f7a;
    --navy-dark: #17315f;
    --ink: #2b2f38;
    --paper: #ffffff;
    --backdrop: #e9e6e0;
    --rule: #d9dee8;
  }
  * { box-sizing: border-box; margin: 0; padding: 0; }
  html, body {
    width: 1200px; height: 950px; overflow: hidden;
    background: var(--backdrop);
    font-family: "Arimo", Arial, sans-serif;
  }
  .sheet {
    width: 1200px; height: 950px;
    display: flex; flex-direction: column; align-items: center; justify-content: center;
    gap: 50px;
  }
  .card {
    width: 700px; height: 400px;
    background: var(--paper);
    position: relative;
    overflow: hidden;
    box-shadow: 0 4px 14px rgba(0,0,0,.18);
  }
  /* Front */
  .card--front .brand {
    position: absolute; top: 95px; left: 0; right: 0;
    text-align: center;
  }
  .wordmark {
    font-weight: 700; color: var(--navy);
    font-size: 112px; line-height: 1; letter-spacing: 2px;
  }
  .brand__url {
    margin-top: 10px;
    font-size: 15px; letter-spacing: 4px; color: var(--navy);
  }
  .tagline {
    position: absolute; bottom: 42px; left: 0; right: 0;
    text-align: center; font-size: 17px; font-weight: 700; color: var(--ink);
  }
  /* Back */
  .card--back .brand {
    position: absolute; top: 40px; left: 0; right: 0; text-align: center;
  }
  .card--back .wordmark { font-size: 104px; }
  .band {
    position: absolute; left: 0; right: 0; bottom: 0; height: 215px;
    background: linear-gradient(180deg, var(--navy) 0%, var(--navy-dark) 100%);
    display: flex; align-items: center; justify-content: center;
  }
  .band::before, .band::after {
    content: ""; position: absolute; left: 0; right: 0; height: 3px; background: var(--rule);
  }
  .band::before { top: 8px; }
  .band::after { bottom: 8px; }
  .person {
    text-align: right; color: var(--paper); padding-right: 22px;
    border-right: 1.5px solid rgba(255,255,255,.85);
  }
  .person__name { font-size: 22px; font-weight: 700; margin-bottom: 6px; }
  .person__line { font-size: 16px; line-height: 1.45; }
  .contact { list-style: none; padding-left: 22px; color: var(--paper); font-size: 16px; }
  .contact li { display: flex; align-items: center; gap: 10px; line-height: 1.65; }
  .contact svg { width: 16px; height: 16px; fill: var(--paper); flex: none; }
</style>
</head>
<body>
<main class="sheet">
  <section class="card card--front">
    <div class="brand">
      <div class="wordmark">DK&amp;R</div>
      <div class="brand__url">www.dkrfabworks.example</div>
    </div>
    <p class="tagline">We provide Project Management &amp; Project Support Services</p>
  </section>

  <section class="card card--back">
    <div class="brand"><div class="wordmark">DK&amp;R</div></div>
    <div class="band">
      <div class="person">
        <div class="person__name">Glenn Harwick</div>
        <div class="person__line">Business Development Manager</div>
        <div class="person__line">418 Wendlow Ridge Drive, Suite 340</div>
        <div class="person__line">Birmingham, AL 35242</div>
      </div>
      <ul class="contact">
        <li><svg viewBox="0 0 16 16"><path d="M3 2h3l1.5 3.5-2 1.3a8 8 0 0 0 3.7 3.7l1.3-2L14 10v3a1 1 0 0 1-1 1A11 11 0 0 1 2 3a1 1 0 0 1 1-1z"/></svg>205-555-0163</li>
        <li><svg viewBox="0 0 16 16"><path d="M4.5 1h7a1 1 0 0 1 1 1v12a1 1 0 0 1-1 1h-7a1 1 0 0 1-1-1V2a1 1 0 0 1 1-1zm.5 2v9h6V3zm3 10a.8.8 0 1 0 0 1.6.8.8 0 0 0 0-1.6z"/></svg>205-555-0164</li>
        <li><svg viewBox="0 0 16 16"><path d="M1 3.5h14v9H1zm1.5 1.2L8 9l5.5-4.3v-.2h-11z"/></svg>glenn@dkrfabworks.example</li>
        <li><svg viewBox="0 0 16 16"><path d="M8 1a7 7 0 1 0 0 14A7 7 0 0 0 8 1zm0 1.5c.8 0 1.7 1.6 2 4H6c.3-2.4 1.2-4 2-4zM5.9 8h4.2c0 .6 0 1-.1 1.5H6c-.1-.5-.1-.9-.1-1.5zM3 8h1.4c0 .5 0 1 .1 1.5H3.2A5 5 0 0 1 3 8zm8.6 0H13a5 5 0 0 1-.2 1.5h-1.3c.1-.5.1-1 .1-1.5zM6.2 11h3.6c-.4 1.6-1.1 2.5-1.8 2.5s-1.4-.9-1.8-2.5z"/></svg>www.dkrfabworks.example</li>
      </ul>
    </div>
  </section>
</main>
</body>
</html>
```